Design professional label for greener chemicals (cleaning and lubrication) brand

Design a b2b professional label that is based on the examples given.
Size: 135 x 200 mm, please use text of the label description doc (only the kaltro stainless steel polish example design document has the right text and size)
It should include:
1. Logo, can be fully changed except the shape of "KALTRO", colors and fonts of the rest can be customized
2. Focus should be on professional market, we would like to express the professionalism and high quality of the product
3. Focus should be on our brand name "KALTRO BRIGHTER COMPOUNDS"
4. Should include product name, product description, danger sentences, danger symbol, user instructions, image
5. Should include numbers that explain what the product does: 1. Prewash 2. Clean 3. Protect 4. Preserve and highlight number 2.

Target Market(s)

Professional cleaning companies, steel industry, food industry, pharmacy industry

Industry/Entity Type

Cleaning industry, steel industry, food industry, boat cleaning, car cleaning, professional lubrication

Font styles to use
Sans Serif

Requirements
Must have
• Professional look, clean look, image, focus on our brand name
Nice to have
• Numbers (see explanation), label divided in three parts (logo and product name and image in the middle as the highlight)

```html
<!DOCTYPE html>
<html lang="en">
<head>
<meta charset="utf-8">
<title>Kaltro Stainless Steel Polish – Label</title>
<link rel="stylesheet" href="https://fonts.googleapis.com/css2?family=Oswald:wght@500;700&family=Fira+Sans+Condensed:wght@400;600&family=Poppins:wght@800&display=swap">
<style>
  :root{
    --bg:#e9f8dd;
    --navy:#23346f;
    --navy-dark:#1a2654;
    --green:#86c846;
    --green-light:#a6d96c;
    --red:#b3372e;
    --white:#ffffff;
    --steel-1:#f4f4f4;
    --steel-2:#9aa0a6;
  }
  *{box-sizing:border-box;margin:0;padding:0}
  html,body{width:1147px;height:1200px;overflow:hidden;background:var(--bg)}
  body{position:relative;font-family:"Fira Sans Condensed",sans-serif;color:var(--white)}

  .label-panel{position:absolute;top:243px;width:220px;height:374px;overflow:hidden;background:var(--navy)}
  .label-panel--back-left{left:127px}
  .label-panel--front{left:473px}
  .label-panel--back-right{left:801px}

  .panel-top-strip{position:absolute;left:0;top:0;width:100%;height:13px;background:var(--white)}
  .panel-blue{position:absolute;left:0;top:13px;width:100%;height:235px;
    background:radial-gradient(ellipse at 50% 40%,#2f448a 0%,var(--navy) 70%)}
  .panel-red-line{position:absolute;left:0;top:248px;width:100%;height:5px;background:var(--red)}
  .panel-green{position:absolute;left:0;top:253px;width:100%;height:114px;
    background:linear-gradient(180deg,var(--green-light),var(--green))}
  .panel-bottom-strip{position:absolute;left:0;bottom:0;width:100%;height:7px;background:var(--navy-dark)}

  /* front */
  .brand-box{position:absolute;left:29px;top:13px;width:162px;height:93px;background:var(--white);
    border-radius:0 0 10px 10px;text-align:center;padding-top:4px}
  .brand-tagline{font-family:"Oswald",sans-serif;font-weight:700;font-size:7.4px;color:var(--navy);letter-spacing:-.1px}
  .brand-name{font-family:"Oswald",sans-serif;font-weight:700;font-size:40px;line-height:48px;color:var(--navy);letter-spacing:1px}
  .brand-sub{font-family:"Oswald",sans-serif;font-weight:700;font-size:11px;color:var(--navy);letter-spacing:1.2px;margin-top:-2px}
  .product-title{position:absolute;left:0;top:142px;width:100%;text-align:center;font-family:"Oswald",sans-serif;font-weight:700;
    font-size:38px;line-height:44px;color:#e6e8ea;letter-spacing:-1.5px;transform:scaleX(.82)}
  .step-list{position:absolute;left:58px;top:268px;list-style:none}
  .step-list li{display:flex;align-items:center;gap:6px;height:20px;margin-bottom:3.5px;padding:0 8px 0 5px;border-radius:10px;
    font-family:"Poppins",sans-serif;font-weight:800;font-size:11.5px;color:var(--navy);letter-spacing:.5px}
  .step-list li.step--highlight{background:var(--navy);color:var(--white)}
  .step-num{width:13px;height:13px;border-radius:50%;background:var(--red);border:1.5px solid var(--navy);color:var(--white);font-size:7px;
    display:flex;align-items:center;justify-content:center;letter-spacing:0;flex:none}
  .step--highlight .step-num{border-color:var(--white)}
  .hazard-set{position:absolute}
  .label-panel--front .hazard-set{left:186px;top:268px}

  /* back left */
  .usage-tag{position:absolute;left:30px;top:26px;width:106px;height:23px;background:var(--red);text-align:center;
    font-family:"Oswald",sans-serif;font-weight:700;font-size:7.6px;line-height:9px;padding-top:2px}
  .usage-photo{position:absolute;left:30px;top:49px;width:106px;height:101px;
    background:linear-gradient(135deg,var(--steel-1) 0%,#c9cdd1 35%,var(--steel-2) 60%,#d8dbde 100%)}
  .product-description{position:absolute;left:26px;top:176px;width:120px;font-size:6.5px;line-height:10px}
  .producer-info{position:absolute;left:24px;top:266px;width:130px;font-size:6.2px;line-height:9.2px;color:var(--navy-dark)}
  .producer-info strong{font-weight:600}
  .label-number{margin-top:9px}

  /* back right */
  .instructions{position:absolute;left:46px;top:35px;width:110px}
  .instructions h3{font-family:"Oswald",sans-serif;font-weight:700;font-size:7.6px;margin-bottom:7px}
  .instructions ul{list-style:none}
  .instructions li{position:relative;padding-left:8px;font-size:7.4px;line-height:10px;margin-bottom:4px}
  .instructions li::before{content:"";position:absolute;left:0;top:3px;width:4px;height:4px;border-radius:50%;background:#c6cde0}
  .batch-info{position:absolute;left:53px;top:213px;font-size:6.4px;line-height:9.5px}
  .danger-text{position:absolute;left:46px;top:272px;width:108px;font-size:6.4px;line-height:9.6px;color:var(--navy-dark);text-align:justify}
  .danger-text strong{font-weight:600}
  .label-panel--back-right .hazard-set{left:16px;top:274px}

  /* brand lockup */
  .brand-lockup{position:absolute;left:0;top:820px;width:100%;text-align:center}
  .lockup-name{font-family:"Oswald",sans-serif;font-weight:700;font-size:236px;line-height:230px;color:var(--navy);letter-spacing:6px}
  .lockup-sub{font-family:"Oswald",sans-serif;font-weight:700;font-size:60px;line-height:70px;color:var(--navy);letter-spacing:8px;margin-top:14px}
</style>
</head>
<body>

<section class="label-panel label-panel--back-left">
  <div class="panel-top-strip"></div>
  <div class="panel-blue"></div>
  <div class="usage-tag">USED FOR STAINLESS STEEL<br>INDUSTRIAL SURFACES</div>
  <div class="usage-photo" role="img" aria-label="Photo of stainless steel industrial piping"></div>
  <p class="product-description">Lumarex is a mildly abrasive cleansing cream with preservative properties. For removing stubborn dirt, water stains and deposits on stainless steel with a hologram free finish. Lumarex is non-tox and safe to use.</p>
  <div class="panel-red-line"></div>
  <div class="panel-green"></div>
  <div class="producer-info">
    <p>Produced by <strong>Kaltro Laboratories Int. B.V.</strong></p>
    <p>Postbus 20481 - 5100 AB Dalmeer (NL)</p>
    <p>Phone NL: +31 400 12 34 56</p>
    <p>Lindenlaan 42 bus 8 - 3600 Hoverdal (B)</p>
    <p>Phone B: +32 10 00 12 34</p>
    <p>www.kaltrocompounds.example</p>
    <p>hello@kaltrocompounds.example</p>
    <p class="label-number">Label number: 23092021</p>
  </div>
  <div class="panel-bottom-strip"></div>
</section>

<section class="label-panel label-panel--front">
  <div class="panel-top-strip"></div>
  <div class="panel-blue"></div>
  <div class="brand-box">
    <p class="brand-tagline">RESTORE STEEL SURFACES HOLOGRAM FREE</p>
    <p class="brand-name">KALTRO</p>
    <p class="brand-sub">BRIGHTER COMPOUNDS</p>
  </div>
  <h1 class="product-title">STAINLESS<br>STEEL POLISH</h1>
  <div class="panel-red-line"></div>
  <div class="panel-green"></div>
  <ol class="step-list">
    <li><span class="step-num">1</span>PREWASH</li>
    <li class="step--highlight"><span class="step-num">2</span>CLEAN</li>
    <li><span class="step-num">3</span>PROTECT</li>
    <li><span class="step-num">4</span>PRESERVE</li>
  </ol>
  <svg class="hazard-set" width="22" height="32" viewBox="0 0 22 32" aria-label="Hazard pictograms">
    <g fill="#fff" stroke="#c0392b" stroke-width="1.2">
      <rect x="6" y="2" width="9" height="9" transform="rotate(45 10.5 6.5)"/>
      <rect x="2" y="12" width="9" height="9" transform="rotate(45 6.5 16.5)"/>
      <rect x="11" y="12" width="9" height="9" transform="rotate(45 15.5 16.5)"/>
      <rect x="6" y="21" width="9" height="9" transform="rotate(45 10.5 25.5)"/>
    </g>
  </svg>
  <div class="panel-bottom-strip"></div>
</section>

<section class="label-panel label-panel--back-right">
  <div class="panel-top-strip"></div>
  <div class="panel-blue"></div>
  <div class="instructions">
    <h3>USER INSTRUCTIONS:</h3>
    <ul>
      <li>Shake before use.</li>
      <li>Apply with a damp brush, sponge or pad.</li>
      <li>Adjust rubbing pressure and duration to the persistence of the soiling.</li>
      <li>Add water as needed while rubbing, rub in the direction of the structure.</li>
      <li>Rinse with clean water.</li>
    </ul>
  </div>
  <p class="batch-info">Batch number: see packaging.<br>Net volume: see packaging.</p>
  <div class="panel-red-line"></div>
  <div class="panel-green"></div>
  <svg class="hazard-set" width="26" height="36" viewBox="0 0 26 36" aria-label="Hazard pictograms">
    <g fill="#fff" stroke="#c0392b" stroke-width="1.3">
      <rect x="7.5" y="2" width="11" height="11" transform="rotate(45 13 7.5)"/>
      <rect x="2" y="12.5" width="11" height="11" transform="rotate(45 7.5 18)"/>
      <rect x="13" y="12.5" width="11" height="11" transform="rotate(45 18.5 18)"/>
      <rect x="7.5" y="23" width="11" height="11" transform="rotate(45 13 28.5)"/>
    </g>
  </svg>
  <p class="danger-text"><strong>Danger:</strong> Causes severe skin burns and eye damage. Wear protective gloves, protective clothing, eye protection, face protection. IF SWALLOWED: rinse mouth – DO NOT induce vomiting. Immediately call a POISON CENTER, a physician. IF ON SKIN (or hair): Take off immediately all contaminated clothing.</p>
  <div class="panel-bottom-strip"></div>
</section>

<section class="brand-lockup">
  <p class="lockup-name">KALTRO</p>
  <p class="lockup-sub">BRIGHTER COMPOUNDS</p>
</section>

</body>
</html>
```